Business Card for a Renewable energy construction company

I need a formal, neat looking business card. Minimal and professional looking. Back side can have a design that is semi-ransparent/shaded

Target Market(s)

Renewable energy companies

Contact Information for Business Card

Name, Surname and contact details (phone, email)

Colors
00AB8E
00BBA5
67D7C9
C6EFE9
E9F9F6

Requirements
Must have
• Place for a QR code in the back side

```html
<!DOCTYPE html>
<html lang="en">
<head>
<meta charset="utf-8">
<title>Kelvara Business Card</title>
<link rel="stylesheet" href="https://fonts.googleapis.com/css2?family=Lato:wght@400;700;900&display=swap">
<style>
  :root {
    --stage: #232427;
    --card-dark: #151618;
    --card-dark-soft: #1d1e21;
    --card-light: #ffffff;
    --teal: #00ab8e;
    --teal-mid: #00bba5;
    --teal-light: #67d7c9;
    --teal-pale: #c6efe9;
    --ink: #1a1a1a;
    --muted: #6b6b6b;
    --rule: #e2e2e2;
  }
  * { box-sizing: border-box; margin: 0; padding: 0; }
  html, body { width: 1200px; height: 952px; overflow: hidden; }
  body {
    background: var(--stage);
    font-family: "Lato", sans-serif;
    position: relative;
  }
  .card {
    position: absolute;
    left: 250px;
    width: 700px;
    height: 400px;
    overflow: hidden;
    box-shadow: 0 18px 40px rgba(0,0,0,0.45);
  }
  /* Back side */
  .card-back {
    top: 56px;
    background: linear-gradient(160deg, var(--card-dark) 0%, var(--card-dark-soft) 45%, var(--card-dark) 55%, var(--card-dark-soft) 100%);
  }
  .back-shade {
    position: absolute;
    inset: 0;
    background: linear-gradient(115deg, transparent 30%, rgba(255,255,255,0.035) 30%, rgba(255,255,255,0.035) 60%, transparent 60%);
  }
  .brand {
    display: flex;
    align-items: center;
    gap: 14px;
    font-weight: 900;
    letter-spacing: 4px;
  }
  .brand-mark {
    width: 18px;
    height: 18px;
    background: var(--teal);
  }
  .card-back .brand {
    position: absolute;
    left: 50%;
    top: 46%;
    transform: translate(-50%, -50%);
    font-size: 54px;
    color: #ffffff;
  }
  .card-back .brand-mark { width: 24px; height: 24px; }
  .qr-space {
    position: absolute;
    right: 40px;
    bottom: 40px;
    width: 92px;
    height: 92px;
    border: 2px solid rgba(103, 215, 201, 0.55);
    background: rgba(198, 239, 233, 0.06);
  }
  /* Front side */
  .card-front {
    top: 496px;
    background: var(--card-light);
  }
  .band-top {
    position: absolute;
    left: 0; top: 0;
    width: 150px; height: 16px;
    background: var(--teal);
  }
  .band-bottom {
    position: absolute;
    right: 0; bottom: 0;
    width: 170px; height: 24px;
    background: var(--teal);
  }
  .card-front .brand {
    position: absolute;
    left: 56px; top: 128px;
    font-size: 38px;
    color: var(--ink);
  }
  .divider {
    position: absolute;
    left: 318px; top: 80px;
    width: 1px; height: 190px;
    background: var(--rule);
  }
  .person {
    position: absolute;
    left: 352px; top: 96px;
  }
  .person-name {
    font-size: 27px;
    font-weight: 400;
    letter-spacing: 1px;
    color: var(--ink);
    text-transform: uppercase;
  }
  .person-name strong { color: var(--teal); font-weight: 900; }
  .person-title {
    font-size: 17px;
    color: var(--muted);
    margin-top: 4px;
  }
  .contacts {
    list-style: none;
    margin-top: 22px;
    font-size: 16px;
    color: var(--muted);
  }
  .contacts li {
    display: flex;
    align-items: center;
    gap: 10px;
    height: 26px;
  }
  .contacts svg { width: 15px; height: 15px; fill: var(--ink); flex: none; }
  .address {
    position: absolute;
    left: 56px; bottom: 56px;
    font-size: 15px;
    color: var(--muted);
  }
</style>
</head>
<body>
  <section class="card card-back" aria-label="Card back">
    <div class="back-shade"></div>
    <div class="brand"><span class="brand-mark"></span>KELVARA</div>
    <div class="qr-space" role="img" aria-label="Space reserved for QR code"></div>
  </section>

  <section class="card card-front" aria-label="Card front">
    <div class="band-top"></div>
    <div class="band-bottom"></div>
    <div class="brand"><span class="brand-mark"></span>KELVARA</div>
    <div class="divider"></div>
    <div class="person">
      <h1 class="person-name">Daniel R. <strong>Marlowe</strong></h1>
      <p class="person-title">Managing Director</p>
      <ul class="contacts">
        <li>
          <svg viewBox="0 0 24 24" aria-hidden="true"><path d="M6.6 10.8a15 15 0 0 0 6.6 6.6l2.2-2.2c.3-.3.7-.4 1-.2 1.1.4 2.3.6 3.6.6.6 0 1 .4 1 1V20c0 .6-.4 1-1 1A17 17 0 0 1 3 4c0-.6.4-1 1-1h3.5c.6 0 1 .4 1 1 0 1.3.2 2.5.6 3.6.1.3 0 .7-.2 1z"/></svg>
          +00 987 654 32
        </li>
        <li>
          <svg viewBox="0 0 24 24" aria-hidden="true"><path d="M2 5h20v14H2zm2 2v.5l8 5 8-5V7l-8 5z"/></svg>
          hello@kelvaramail.com
        </li>
        <li>
          <svg viewBox="0 0 24 24" aria-hidden="true"><path d="M12 2a10 10 0 1 0 0 20 10 10 0 0 0 0-20zm6.9 6h-3a15 15 0 0 0-1.3-3.9A8 8 0 0 1 18.9 8zM12 4c.8 1.2 1.5 2.5 1.9 4h-3.8c.4-1.5 1.1-2.800 1.9-4zM4.3 14a8 8 0 0 1 0-4h3.4a16 16 0 0 0 0 4zm.8 2h3a15 15 0 0 0 1.3 3.9A8 8 0 0 1 5.1 16zm3-8h-3a8 8 0 0 1 4.3-3.9C8.8 5.3 8.4 6.6 8.1 8zM12 20c-.8-1.2-1.5-2.5-1.900-4h3.8c-.4 1.5-1.100 2.8-1.900 4zm2.3-6H9.7a14 14 0 0 1 0-4h4.6a14 14 0 0 1 0 4zm.3 5.9c.6-1.2 1-2.5 1.3-3.9h3a8 8 0 0 1-4.3 3.9zm1.7-5.9a16 16 0 0 0 0-4h3.4a8 8 0 0 1 0 4z"/></svg>
          www.kelvaraenergy.com
        </li>
      </ul>
    </div>
    <p class="address">1270 Harbor Ridge Avenue Portland, OR 97205</p>
  </section>
</body>
</html>
```